Web Design Project

We need a design for the actual web.
http://mirela.vunto.example/
It will be a cakes and cupcakes online shop.

It is a one page site, with five anchors.

Inicio (Home)
Here it will show a brief explanation about our shop, just explaining we sell really nice cakes and cupcakes. Also we want to show a slide gallery, like the one it is working, but with not nice choosen pictures.

Productos/Tortas
This two anchors will be just one at the end, but I wanted to show the two options for accessing the different products, tabs or buttons. You can click on the firsts images on that links for see the "pop up image" with a better explanation of every product.

Contacto
Here it will show a little form, that will only appear in smartphones and maybe tablets, this form needs to be similar and much more simple than the principal form (the next anchor), so just focus on it once the next one its done.

Form
This will be the way the users will send the orders, its a complex form, focused on the UX. We dont want the user to type too much and we want it to surprise the user and fell really comfortable.

Industry/Entity Type

Tv

Requirements
Must have

• -Must have side menu, but you can redesign it completelly, but with the same structure
-Its important to focus all the content in the top and middle, we arent sure about users screens and it we set info at the footer, maybe its not gonna show (no scroll vertical).
-You can change all the colours of the site, we are open to new visions, you can surprise us.

```html
<!DOCTYPE html>
<html lang="es">
<head>
<meta charset="utf-8">
<title>Dulce Mirela – Cupcakes y Pasteles</title>
<link rel="stylesheet" href="https://fonts.googleapis.com/css2?family=Parisienne&family=Norican&family=PT+Sans&display=swap">
<style>
:root{
  --cream:#fbf6ea;
  --stripe:#f3ecdc;
  --aqua:#18d6d6;
  --footer-aqua:#08f5f2;
  --teal:#159c9a;
  --teal-dark:#0e7f7d;
  --nav-brown:#a86a55;
  --nav-red:#d3172d;
  --choc:#6e3a24;
  --body-brown:#4a3a30;
  --white:#ffffff;
}
*{box-sizing:border-box;margin:0;padding:0}
html,body{width:1200px;height:1121px;overflow:hidden}
body{
  position:relative;
  background:var(--cream) repeating-linear-gradient(90deg,var(--cream) 0 9px,var(--stripe) 9px 18px);
  font-family:"PT Sans",Arial,sans-serif;
}
.topbar{position:absolute;left:0;top:0;width:1200px;height:44px;background:var(--aqua)}
.topbar-scallop{
  position:absolute;left:0;top:43px;width:1200px;height:13px;
  background:radial-gradient(circle at 12px 0,var(--aqua) 12px,transparent 12.5px) 0 0/24px 13px repeat-x;
}
.main-nav{position:absolute;top:8px;left:140px;display:flex}
.main-nav a{
  font-family:"Norican",cursive;font-size:26px;color:var(--nav-brown);text-decoration:none;
  text-shadow:1px 1px 1px rgba(60,30,20,.45);margin-right:48px;line-height:36px
}
.main-nav a.active{color:var(--nav-red)}
.social{position:absolute;top:6px;right:108px;display:flex;gap:10px}
.social a{
  width:40px;height:40px;border-radius:50%;background:#2f7fc4;border:2px solid var(--white);
  color:var(--white);font-family:"PT Sans",Arial,sans-serif;font-size:9px;text-decoration:none;
  display:flex;align-items:center;justify-content:center;overflow:hidden
}
.social a.friends{background:#3b5a9e}
.site-title{
  position:absolute;left:133px;top:62px;width:960px;
  font-family:"Parisienne",cursive;font-weight:400;font-size:53px;color:var(--teal);
  line-height:76px;white-space:nowrap;letter-spacing:1.2px
}
.side-treats{position:absolute;top:136px;width:48px;height:200px;border-radius:18px;
  background:linear-gradient(180deg,#d8262f 0,#f1e2cc 30%,#b77a45 70%,#7a4525 100%)}
.side-treats.left{left:86px}
.side-treats.right{left:1080px;background:linear-gradient(180deg,#d8262f 0,#5a2b1b 35%,#c5121e 55%,#d9b88a 100%)}
.slider{
  position:absolute;left:128px;top:146px;width:960px;height:416px;background:var(--white);
  box-shadow:0 10px 8px -6px rgba(0,0,0,.35)
}
.slide-photo{
  position:absolute;left:6px;top:5px;width:949px;height:406px;
  background:radial-gradient(ellipse at 45% 45%,#7a3f1e 0,#5a2c14 30%,#b07438 55%,#e9c58c 80%,#f3dcae 100%)
}
.slide-caption{
  position:absolute;left:496px;top:47px;width:438px;height:227px;
  background:rgba(236,205,160,.72);padding:14px 18px 0 22px
}
.slide-caption h2{
  font-family:"Parisienne",cursive;font-weight:400;font-size:40px;color:var(--teal-dark);line-height:48px;
  white-space:nowrap
}
.slide-caption p{
  margin-top:22px;font-family:Arial,Helvetica,sans-serif;font-size:17px;line-height:23px;
  color:var(--body-brown);text-align:justify
}
.btn-more{
  position:absolute;left:276px;top:182px;width:107px;height:35px;border-radius:3px;
  background:var(--choc);color:var(--white);font-family:Arial,Helvetica,sans-serif;font-size:17px;
  line-height:35px;text-align:center;text-decoration:none;box-shadow:0 1px 2px rgba(0,0,0,.4)
}
.ribbon{position:absolute;left:940px;top:133px;width:170px;height:160px;overflow:visible}
.ribbon-label{font-family:"Norican",cursive;font-size:25px;fill:var(--choc)}
.arrow{position:absolute;top:432px}
.arrow.prev{left:108px}
.arrow.next{left:1073px}
.intro{position:absolute;left:133px;top:626px;width:942px}
.intro p{
  font-family:"Parisienne",cursive;font-size:44px;line-height:36px;color:var(--teal);
  letter-spacing:.8px;text-align:justify;text-align-last:left;margin-bottom:36px
}
.footer{position:absolute;left:0;top:1087px;width:1200px;height:34px;background:var(--footer-aqua)}
.copyright{position:absolute;left:126px;top:8px;font-size:15px;color:#222}
.footer-nav{position:absolute;right:117px;top:6px;display:flex;gap:34px}
.footer-nav a{font-family:"Norican",cursive;font-size:17px;color:var(--nav-brown);text-decoration:none}
.footer-nav a.active{color:var(--nav-red)}
</style>
</head>
<body>
<header>
  <div class="topbar">
    <nav class="main-nav">
      <a class="active" href="#inicio">Inicio</a>
      <a href="#productos">Productos</a>
      <a href="#tortas">Tortas</a>
      <a href="#contacto">Contacto</a>
      <a href="#form">Form</a>
    </nav>
    <div class="social">
      <a href="#" aria-label="Pío">Pío</a>
      <a class="friends" href="#" aria-label="Amigos">Amigos</a>
    </div>
  </div>
  <div class="topbar-scallop"></div>
</header>

<h1 class="site-title">Los mejores Cupcakes y Pasteles de Santiago</h1>

<div class="side-treats left" role="img" aria-label="Candy swirl, cake slices and muffin decoration"></div>
<div class="side-treats right" role="img" aria-label="Candy swirl, chocolate cake, cherry and cookie decoration"></div>

<section class="slider" id="inicio">
  <div class="slide-photo" role="img" aria-label="Chocolate-curl cake with a shop tag on a plate"></div>
  <div class="slide-caption">
    <h2>About Dulce Mirela</h2>
    <p>Sed sed enim dolor, eget fringilla erat. Sed quam velit, rutrum vitae ullamcorper quis, pulvinar sed diam. Maecenas adipiscing auctor placerat.</p>
    <a class="btn-more" href="#productos">Learn More</a>
  </div>
</section>

<svg class="ribbon" viewBox="0 0 170 160" aria-label="learn more">
  <defs>
    <linearGradient id="ribbonShade" x1="0" y1="0" x2="1" y2="1">
      <stop offset="0" stop-color="#5fe3e0"/>
      <stop offset="1" stop-color="#109a9a"/>
    </linearGradient>
  </defs>
  <polygon points="8,14 22,8 28,18" fill="#0b5e5e"/>
  <polygon points="150,140 162,148 154,154" fill="#0b5e5e"/>
  <polygon points="15,6 55,2 168,118 160,152" fill="url(#ribbonShade)"/>
  <text class="ribbon-label" x="0" y="0" text-anchor="middle" dominant-baseline="central"
        transform="translate(100,70) rotate(45)">learn more</text>
</svg>

<svg class="arrow prev" width="34" height="66" viewBox="0 0 34 66" aria-label="Anterior">
  <path d="M32 2 Q6 12 2 33 Q6 54 32 64 Z" fill="#a89483" stroke="#e8ddd0" stroke-width="2"/>
  <path d="M22 27 H14 V22 L6 33 L14 44 V39 H22 Z" fill="#6d5a4b"/>
</svg>
<svg class="arrow next" width="34" height="66" viewBox="0 0 34 66" aria-label="Siguiente">
  <path d="M2 2 Q28 12 32 33 Q28 54 2 64 Z" fill="#a89483" stroke="#e8ddd0" stroke-width="2"/>
  <path d="M12 27 H20 V22 L28 33 L20 44 V39 H12 Z" fill="#6d5a4b"/>
</svg>

<section class="intro">
  <p>Finalmente ya está disponible en Santiago de Chile nuestro catálogo de sabrosos Cupcakes y Tortas</p>
  <p>Con ingredientes 100% naturales y elaborados artesanalmente</p>
  <p>No solo hay que tener en cuenta la presentación fabulosa de los mismos, lo que más destacan nuestros clientes es el sabor exquisito y la textura</p>
</section>

<footer class="footer">
  <div class="copyright">© 2012 Dulce Mirela. All Rights Reserved.</div>
  <nav class="footer-nav">
    <a class="active" href="#inicio">Inicio</a>
    <a href="#productos">Productos</a>
    <a href="#tortas">Tortas</a>
    <a href="#contacto">Contacto</a>
    <a href="#form">Form</a>
  </nav>
</footer>
</body>
</html>
```